Business Card for Marco Thieblin Analytics and Marco Thieblin Photography

I want a double sided business card: on one side it should be about "Marco Thieblin Photography" and on the other side about "Marco Thieblin Analytics". You find the logos for these two projects in the attachments. The design of the business card should blend well with the colours and fonts used in the logos and should be quite simple, yet look professional and modern.

In addition to my name, there should be content for a telephone number, e-mail address and website. There should be little icons (for telephone, email and web) before these fields. I do not want a postal mail address field.
Lastly you should indicate that people can contact me in the following languages: Lëtzebuergesch, Deutsch, Français, English, Castellano, Ido
This should be very unobtrusive: either in a small muted font or with little icons (preferably without using flags as flags represent nations, not languages - one possibility would be by using the 2 letter ISO codes).

The design should be delivered in Adobe Illustrator format or something similar that I can edit easily, as it's possible that I will change my e-mail address and domain soon.

I hope this was detailed enough but still leaves you some freedom for designing something nice.

Thank you!
Marco

Industry/Entity Type

Business

Contact Information for Business Card

e-mail address: mtb_@orvenmail.example
website: www.marcothieblin.example (for Marco Thieblin Photography)
website: kelvodata.example/mtb (for Marco Thieblin Analytics - this address is likely to change)
phone: +352 691 987 654 (not my real number - I prefer not to publish it on the web)

Requirements
Nice to have
• A speech bubble followed by the 2-letter language codes (lb, de, fr, en, es, io) or even speech bubble icons for every language would be nice and eliminates the need to put text like 'you can contact me in the following languages'.

```html
<!DOCTYPE html>
<html lang="en">
<head>
<meta charset="utf-8">
<title>Marco Thieblin – Business Cards</title>
<link rel="stylesheet" href="https://fonts.googleapis.com/css2?family=Open+Sans:wght@400;600;700&display=swap">
<style>
  :root {
    --page: #e8eaec;
    --card: #ffffff;
    --ink: #5a5f66;
    --muted: #8a8f96;
    --night: #050505;
    --accent-orange: #e98a2c;
    --blue: #1d96dd;
    --blue-light: #3fb4f2;
    --blue-deep: #0f74b8;
    --green: #1fa84a;
    --green-light: #6cc84a;
    --green-deep: #137d35;
  }
  * { box-sizing: border-box; margin: 0; padding: 0; }
  html, body { width: 1200px; height: 2191px; overflow: hidden; }
  body {
    background: var(--page);
    font-family: "Open Sans", Arial, sans-serif;
    color: var(--ink);
    position: relative;
  }
  .card {
    position: absolute;
    left: 100px;
    width: 1000px;
    height: 580px;
    background: var(--card);
    box-shadow: 0 8px 28px rgba(0,0,0,.14);
    overflow: hidden;
  }
  .card--photography { top: 270px; --theme: var(--blue); --theme-light: var(--blue-light); --theme-deep: var(--blue-deep); }
  .card--analytics { top: 1340px; --theme: var(--green); --theme-light: var(--green-light); --theme-deep: var(--green-deep); }

  .brand-panel {
    position: absolute; left: 0; top: 0; width: 420px; height: 580px;
    display: flex; align-items: center; justify-content: center; gap: 14px;
    padding: 0 30px;
  }
  .card--photography .brand-panel { background: var(--night); }
  .brand-mark { width: 26px; height: 26px; border-radius: 50%; background: var(--accent-orange); flex: none; }
  .brand-name {
    font-weight: 600; font-size: 27px; line-height: 1.2;
    color: var(--accent-orange);
  }

  .ribbon { position: absolute; left: 0; top: 0; width: 1000px; height: 580px; }
  .ribbon .fold { fill: var(--theme-light); }
  .ribbon .band { fill: var(--theme); }
  .ribbon .shade { fill: var(--theme-deep); }

  .holder-name {
    position: absolute; left: 520px; top: 168px; width: 460px;
    font-weight: 700; font-size: 40px; letter-spacing: .5px;
    color: #fff; text-transform: uppercase; white-space: nowrap;
  }

  .contact-list { position: absolute; left: 462px; top: 285px; list-style: none; }
  .contact-item {
    display: flex; align-items: center; gap: 22px;
    height: 64px; font-size: 27px; color: var(--ink);
  }
  .contact-icon { width: 34px; height: 34px; flex: none; }
  .contact-icon .stroke { fill: none; stroke: var(--theme); stroke-width: 2.4; }
  .contact-icon .solid { fill: var(--theme); }

  .languages {
    position: absolute; left: 462px; top: 492px;
    display: flex; align-items: center; gap: 12px;
    font-size: 16px; color: var(--muted);
  }
  .languages__label { margin-right: 8px; }
  .lang {
    width: 44px; height: 38px; position: relative;
    display: flex; align-items: center; justify-content: center;
    font-size: 14px; color: var(--accent-orange);
  }
  .lang svg { position: absolute; inset: 0; }
  .lang svg path { fill: none; stroke: var(--accent-orange); stroke-width: 1.8; }
  .lang span { position: relative; top: -2px; }
</style>
</head>
<body>

<section class="card card--photography" aria-label="Photography side">
  <div class="brand-panel">
    <span class="brand-mark"></span>
    <span class="brand-name">Marco Thieblin Photography</span>
  </div>
  <svg class="ribbon" viewBox="0 0 1000 580" aria-hidden="true">
    <polygon class="fold" points="430,0 480,0 480,150 430,200"/>
    <polygon class="shade" points="430,200 480,150 480,250"/>
    <rect class="band" x="480" y="150" width="520" height="100"/>
    <polygon class="fold" points="440,110 480,150 440,150"/>
  </svg>
  <div class="holder-name">Marco Thieblin</div>
  <ul class="contact-list">
    <li class="contact-item">
      <svg class="contact-icon" viewBox="0 0 34 34"><rect class="stroke" x="3" y="8" width="28" height="19"/><path class="stroke" d="M3 8 L17 19 L31 8"/></svg>
      mtb_@orvenmail.example
    </li>
    <li class="contact-item">
      <svg class="contact-icon" viewBox="0 0 34 34"><circle class="solid" cx="17" cy="17" r="14"/><path d="M3 17h28M17 3c-6 7-6 21 0 28M17 3c6 7 6 21 0 28" fill="none" stroke="#fff" stroke-width="1.6"/></svg>
      www.marcothieblin.example
    </li>
    <li class="contact-item">
      <svg class="contact-icon" viewBox="0 0 34 34"><rect class="stroke" x="9" y="3" width="16" height="28" rx="2"/><circle class="solid" cx="17" cy="27" r="1.6"/></svg>
      +352 691 987 654
    </li>
  </ul>
  <div class="languages">
    <span class="languages__label">Contact me in:</span>
    <span class="lang"><svg viewBox="0 0 44 38"><path d="M22 3c10 0 19 6 19 14s-9 14-19 14c-3 0-5 0-7-1l-8 5 2-7C5 26 3 22 3 17 3 9 12 3 22 3z"/></svg><span>lb</span></span>
    <span class="lang"><svg viewBox="0 0 44 38"><path d="M22 3c10 0 19 6 19 14s-9 14-19 14c-3 0-5 0-7-1l-8 5 2-7C5 26 3 22 3 17 3 9 12 3 22 3z"/></svg><span>de</span></span>
    <span class="lang"><svg viewBox="0 0 44 38"><path d="M22 3c10 0 19 6 19 14s-9 14-19 14c-3 0-5 0-7-1l-8 5 2-7C5 26 3 22 3 17 3 9 12 3 22 3z"/></svg><span>fr</span></span>
    <span class="lang"><svg viewBox="0 0 44 38"><path d="M22 3c10 0 19 6 19 14s-9 14-19 14c-3 0-5 0-7-1l-8 5 2-7C5 26 3 22 3 17 3 9 12 3 22 3z"/></svg><span>es</span></span>
    <span class="lang"><svg viewBox="0 0 44 38"><path d="M22 3c10 0 19 6 19 14s-9 14-19 14c-3 0-5 0-7-1l-8 5 2-7C5 26 3 22 3 17 3 9 12 3 22 3z"/></svg><span>en</span></span>
    <span class="lang"><svg viewBox="0 0 44 38"><path d="M22 3c10 0 19 6 19 14s-9 14-19 14c-3 0-5 0-7-1l-8 5 2-7C5 26 3 22 3 17 3 9 12 3 22 3z"/></svg><span>io</span></span>
  </div>
</section>

<section class="card card--analytics" aria-label="Analytics side">
  <div class="brand-panel">
    <span class="brand-mark"></span>
    <span class="brand-name">Marco Thieblin Analytics</span>
  </div>
  <svg class="ribbon" viewBox="0 0 1000 580" aria-hidden="true">
    <polygon class="fold" points="430,0 480,0 480,150 430,200"/>
    <polygon class="shade" points="430,200 480,150 480,250"/>
    <rect class="band" x="480" y="150" width="520" height="100"/>
    <polygon class="fold" points="440,110 480,150 440,150"/>
  </svg>
  <div class="holder-name">Marco Thieblin</div>
  <ul class="contact-list">
    <li class="contact-item">
      <svg class="contact-icon" viewBox="0 0 34 34"><rect class="stroke" x="3" y="8" width="28" height="19"/><path class="stroke" d="M3 8 L17 19 L31 8"/></svg>
      mtb_@orvenmail.example
    </li>
    <li class="contact-item">
      <svg class="contact-icon" viewBox="0 0 34 34"><circle class="solid" cx="17" cy="17" r="14"/><path d="M3 17h28M17 3c-6 7-6 21 0 28M17 3c6 7 6 21 0 28" fill="none" stroke="#fff" stroke-width="1.6"/></svg>
      kelvodata.example/mtb
    </li>
    <li class="contact-item">
      <svg class="contact-icon" viewBox="0 0 34 34"><rect class="stroke" x="9" y="3" width="16" height="28" rx="2"/><circle class="solid" cx="17" cy="27" r="1.6"/></svg>
      +352 691 987 654
    </li>
  </ul>
  <div class="languages">
    <span class="languages__label">Contact me in:</span>
    <span class="lang"><svg viewBox="0 0 44 38"><path d="M22 3c10 0 19 6 19 14s-9 14-19 14c-3 0-5 0-7-1l-8 5 2-7C5 26 3 22 3 17 3 9 12 3 22 3z"/></svg><span>lb</span></span>
    <span class="lang"><svg viewBox="0 0 44 38"><path d="M22 3c10 0 19 6 19 14s-9 14-19 14c-3 0-5 0-7-1l-8 5 2-7C5 26 3 22 3 17 3 9 12 3 22 3z"/></svg><span>de</span></span>
    <span class="lang"><svg viewBox="0 0 44 38"><path d="M22 3c10 0 19 6 19 14s-9 14-19 14c-3 0-5 0-7-1l-8 5 2-7C5 26 3 22 3 17 3 9 12 3 22 3z"/></svg><span>fr</span></span>
    <span class="lang"><svg viewBox="0 0 44 38"><path d="M22 3c10 0 19 6 19 14s-9 14-19 14c-3 0-5 0-7-1l-8 5 2-7C5 26 3 22 3 17 3 9 12 3 22 3z"/></svg><span>es</span></span>
    <span class="lang"><svg viewBox="0 0 44 38"><path d="M22 3c10 0 19 6 19 14s-9 14-19 14c-3 0-5 0-7-1l-8 5 2-7C5 26 3 22 3 17 3 9 12 3 22 3z"/></svg><span>en</span></span>
    <span class="lang"><svg viewBox="0 0 44 38"><path d="M22 3c10 0 19 6 19 14s-9 14-19 14c-3 0-5 0-7-1l-8 5 2-7C5 26 3 22 3 17 3 9 12 3 22 3z"/></svg><span>io</span></span>
  </div>
</section>

</body>
</html>
```